Kestrel Aid Services Banner Ad

Need a 750 x 250-pixel banner ad with the company Logo included. Please see company website at www.kestrelaidservices.com for more information.

```html
<!DOCTYPE html>
<html lang="en">
<head>
<meta charset="utf-8">
<title>Kestrel Aid Services Banner Ad</title>
<link href="https://fonts.googleapis.com/css2?family=Arimo:wght@400;700&family=Open+Sans:wght@600&display=swap" rel="stylesheet">
<style>
  :root {
    --navy: #14305a;
    --navy-deep: #0b2147;
    --blue-mid: #1d5b97;
    --green: #6ab04c;
    --silver: #c9cbcf;
    --silver-light: #eef0f2;
    --text-grey: #4a4d52;
    --page: #ececec;
    --white: #ffffff;
  }
  html, body {
    margin: 0;
    width: 1200px;
    height: 598px;
    overflow: hidden;
    background: var(--page);
  }
  .banner {
    position: absolute;
    left: 0;
    top: 100px;
    width: 1041px;
    height: 346px;
    transform: scale(1.15274);
    transform-origin: 0 0;
    background: linear-gradient(135deg, var(--white) 55%, var(--silver-light) 100%);
    overflow: hidden;
    font-family: "Arimo", Arial, sans-serif;
  }
  .banner-shapes {
    position: absolute;
    inset: 0;
  }
  .brand {
    position: absolute;
    right: 26px;
    top: 44px;
    display: flex;
    align-items: center;
    gap: 10px;
    color: var(--navy);
    font-weight: 700;
    font-size: 27px;
    letter-spacing: 0.3px;
  }
  .brand-dot {
    width: 30px;
    height: 30px;
    border-radius: 50%;
    background: var(--green);
  }
  .headline {
    position: absolute;
    right: 24px;
    top: 112px;
    margin: 0;
    text-align: right;
    color: var(--navy);
    font-weight: 700;
    font-size: 30px;
    line-height: 35px;
    letter-spacing: 1.3px;
  }
  .mission {
    position: absolute;
    right: 23px;
    top: 194px;
    margin: 0;
    width: 420px;
    text-align: right;
    color: var(--text-grey);
    font-size: 15px;
    line-height: 22.5px;
  }
  .contact-bar {
    position: absolute;
    left: 580px;
    top: 288px;
    width: 461px;
    height: 45px;
    background: linear-gradient(90deg, var(--navy-deep), var(--navy));
    display: flex;
    align-items: center;
    justify-content: center;
    gap: 16px;
    font-family: "Open Sans", Arial, sans-serif;
    font-weight: 600;
    font-size: 10.5px;
    color: var(--white);
  }
  .contact-item {
    display: flex;
    align-items: center;
    gap: 4px;
  }
  .contact-icon {
    width: 10px;
    height: 10px;
  }
</style>
</head>
<body>
  <div class="banner">
    <svg class="banner-shapes" viewBox="0 0 1041 346" width="1041" height="346">
      <defs>
        <linearGradient id="blue-wedge" x1="0" y1="0" x2="1" y2="0">
          <stop offset="0" stop-color="#1d5b97"/>
          <stop offset="1" stop-color="#0b2147"/>
        </linearGradient>
        <linearGradient id="silver-band" x1="0" y1="0" x2="1" y2="1">
          <stop offset="0" stop-color="#f4f5f6"/>
          <stop offset="0.6" stop-color="#c9cbcf"/>
          <stop offset="1" stop-color="#e6e7e9"/>
        </linearGradient>
        <linearGradient id="photo-tones" x1="0" y1="0" x2="1" y2="1">
          <stop offset="0" stop-color="#a4684a"/>
          <stop offset="0.45" stop-color="#c98258"/>
          <stop offset="1" stop-color="#7a5238"/>
        </linearGradient>
      </defs>
      <path d="M225 0 L612 0 Q522 70 500 210 L400 210 Z" fill="url(#blue-wedge)"/>
      <path d="M0 22 Q270 -42 478 48 Q578 130 582 346 L0 346 Z" fill="url(#silver-band)"/>
      <path d="M0 44 Q262 -24 456 57 Q550 134 556 346 L0 346 Z" fill="var(--green)"/>
      <path d="M0 62 Q252 -8 436 66 Q526 140 532 346 L0 346 Z" fill="url(#photo-tones)" role="img" aria-label="Photo of a smiling child in a wheelchair in a library with bookshelves"/>
    </svg>

    <div class="brand">
      <span class="brand-dot"></span>
      <span class="brand-name">Kestrel Aid Services</span>
    </div>

    <h1 class="headline">SUPPORT COORDINATION<br>ACROSS NEW JERSEY</h1>

    <p class="mission">Kestrel Aid Services was founded with a mission; making a positive difference in the lives to the individuals we serve through Support Coordination.</p>

    <div class="contact-bar">
      <span class="contact-item">
        <svg class="contact-icon" viewBox="0 0 10 10"><circle cx="5" cy="5" r="5" fill="#fff"/><rect x="2.3" y="3.2" width="5.4" height="3.6" fill="none" stroke="#14305a" stroke-width="0.8"/><path d="M2.3 3.2 L5 5.3 L7.7 3.2" fill="none" stroke="#14305a" stroke-width="0.8"/></svg>
        info@kestrelaidservices.com
      </span>
      <span class="contact-item">
        <svg class="contact-icon" viewBox="0 0 10 10"><circle cx="5" cy="5" r="4.4" fill="none" stroke="#fff" stroke-width="0.9"/><path d="M3.4 2.9 L4.2 2.7 L4.7 3.9 L4.2 4.4 Q4.8 5.5 5.7 5.9 L6.2 5.4 L7.3 5.9 L7.1 6.7 Q5.6 7.2 4.2 5.8 Q2.9 4.4 3.4 2.9 Z" fill="#fff"/></svg>
        609-555-0142
      </span>
      <span class="contact-item">
        <svg class="contact-icon" viewBox="0 0 10 10"><circle cx="5" cy="5" r="4.4" fill="none" stroke="#fff" stroke-width="0.9"/><ellipse cx="5" cy="5" rx="1.9" ry="4.4" fill="none" stroke="#fff" stroke-width="0.7"/><line x1="0.6" y1="5" x2="9.4" y2="5" stroke="#fff" stroke-width="0.7"/></svg>
        kestrelaidservices.com
      </span>
    </div>
  </div>
</body>
</html>
```